Word Template for official reports

I would like to Word template to use for a research project. The key topic of the research project is: A cyber security toolkit to protect the privacy data/infrastructure of the health care industry.This file will be used by the entire research team (approx. 50 people) to describe the project outcomes and provide that to the Tarvell Council. Therefore, the design should be professional, and official. The fact that the word file will be used by several people for the same project means that the template should allow the user any time (s)he adds a table to have a particular format. Any time the user adds bullet points, these should have a particular colour and shape, and so on. The users have MS windows and MAC. About the word design, you should use the project logo that I am attaching and of course you may use at the layout colors that matches to this logo. Pay attention, we need to keep the file size as low as possible so please avoid adding graphics on each page. Graphics at the cover page are enough. Regarding its structure, I am attaching the basic word (non-professional), without design. You may notice at the bottom of each slide there is the KR flag and a particular phrase beside. Please use that in your proposal as well. You may find images for the KR flag here: https://kestralrealm.example/kestral-realm/about-kr/symbols/flag_en If you need any further clarifications, please do not hesitate to contact me.

```html
<!DOCTYPE html>
<html lang="en">
<head>
<meta charset="utf-8">
<title>VARDEN Deliverable Template</title>
<link rel="stylesheet" href="https://fonts.googleapis.com/css2?family=Open+Sans:ital,wght@0,300;0,400;0,600;0,700;1,400;1,600&display=swap">
<style>
:root{
  --stage:#8c8c8c;
  --paper:#ffffff;
  --teal:#1cb5a9;
  --teal-dark:#119488;
  --teal-soft:#c9f5f1;
  --line:#7fd6cf;
  --ink:#222;
  --muted:#8a9a98;
  --flag:#1f3f95;
}
*{box-sizing:border-box;margin:0;padding:0}
html,body{width:810px;height:1200px;overflow:hidden;background:var(--stage)}
body{position:relative;font-family:"Open Sans",Arial,sans-serif;color:var(--ink)}
.page{position:absolute;background:var(--paper);overflow:hidden}
.cover{left:266px;top:13px;width:277px;height:392px;
  background:linear-gradient(180deg,#f1f1f1 0%,#ffffff 45%,#e9f7f5 72%,#b9e8e2 100%)}
.cover-art{position:absolute;left:90px;top:80px;width:187px;height:240px;
  background:radial-gradient(ellipse at 60% 50%,rgba(120,210,200,.35),rgba(255,255,255,0) 70%)}
.cover-floor{position:absolute;left:0;bottom:0;width:277px;height:90px;
  background:linear-gradient(180deg,rgba(255,255,255,0),rgba(95,200,188,.55))}
.cover-title{position:absolute;left:34px;top:78px;font-size:14px;font-weight:600;color:var(--teal);
  border-bottom:1px solid var(--teal);padding:0 6px 1px 0;line-height:1.1}
.cover-wp{position:absolute;left:35px;top:96px;font-size:10px;font-weight:600;color:var(--teal)}
.cover-version{position:absolute;left:35px;top:111px;font-size:6.5px;font-weight:700;color:var(--teal)}
.cover-brand{position:absolute;left:27px;top:327px;display:flex;align-items:center;gap:5px}
.brand-dot{width:26px;height:26px;border-radius:50%;border:2px solid var(--teal-dark)}
.brand-name{font-family:"Open Sans",Arial,sans-serif;font-weight:300;font-size:18px;color:var(--teal-dark);letter-spacing:1px}
.cover-tagline{position:absolute;left:64px;top:353px;font-size:6.2px;font-weight:300;line-height:1.35;color:var(--teal-dark)}

.inner{width:244px;height:345px}
.p2{left:114px;top:441px}.p3{left:442px;top:441px}.p4{left:114px;top:822px}.p5{left:442px;top:822px}
.side-bar{position:absolute;left:0;top:0;width:11px;height:100%;background:var(--teal)}
.run-head{position:absolute;left:23px;top:12px;width:200px;font-size:3.6px;font-weight:700;color:var(--teal);
  border-bottom:.6px solid var(--line);padding-bottom:2px}
.head-dot{position:absolute;left:216px;top:11px;width:11px;height:11px;border-radius:50%;border:1.2px solid var(--teal-dark)}
.label{position:absolute;left:23px;font-size:4px;font-style:italic;font-weight:600;color:var(--teal)}
.label.plain{color:#555;font-weight:400}
.note{position:absolute;left:23px;width:202px;background:var(--teal-soft);font-size:3.1px;line-height:1.45;padding:3px 2px}
.grid{position:absolute;left:23px;width:202px;border-collapse:collapse;font-size:3.2px}
.grid td,.grid th{border:.5px solid var(--line);padding:0 2px;height:10.6px;vertical-align:middle;text-align:left}
.grid th{background:var(--teal);color:#fff;font-weight:700;height:9px}
.grid .key{font-weight:700;width:74px}
.grid .tall{height:16px}
.grid.history td,.grid.history th{height:10px}
.grid.history .c{text-align:center;font-weight:700}
.foot{position:absolute;left:17px;top:322px;width:214px;border-top:.6px solid var(--line);padding-top:3px;display:flex;align-items:center;gap:4px}
.flag{width:17px;height:11px;background:var(--flag);flex:none}
.foot-text{font-size:2.6px;font-style:italic;color:var(--muted);line-height:1.35;flex:1}
.foot-page{font-size:3px;font-weight:700;color:var(--teal)}
.toc-title{position:absolute;left:0;width:244px;top:33px;text-align:center;font-size:5.6px;font-weight:600;color:var(--teal)}
.toc{position:absolute;left:23px;top:44px;width:202px;list-style:none;font-size:3.3px}
.toc li{display:flex;height:8px;align-items:center;color:#666}
.toc li.lvl1{color:var(--teal);font-weight:600;border-bottom:.5px solid var(--teal)}
.toc li.lvl2{padding-left:4px}
.toc .dots{flex:1;border-bottom:.5px dotted #999;margin:0 1px;height:2px}
.end-brand{position:absolute;left:0;width:244px;top:312px;display:flex;justify-content:center;align-items:center;gap:4px}
.end-brand .brand-dot{width:14px;height:14px;border-width:1.3px}
.end-brand .brand-name{font-size:10px}
.end-band{position:absolute;left:0;bottom:0;width:244px;height:12px;background:var(--teal)}
</style>
</head>
<body>

<section class="page cover">
  <div class="cover-art" role="img" aria-label="Soft teal network of connected nodes and lines"></div>
  <div class="cover-floor"></div>
  <h1 class="cover-title">Deliverable title</h1>
  <p class="cover-wp">WPx– title</p>
  <p class="cover-version">Version: x.x</p>
  <div class="cover-brand"><span class="brand-dot"></span><span class="brand-name">VARDEN</span></div>
  <p class="cover-tagline">An Integrated Cyber Defence Kit For<br>Clinical Networks</p>
</section>

<section class="page inner p2">
  <div class="side-bar"></div>
  <div class="run-head">Dxx: Title</div><span class="head-dot"></span>
  <p class="label" style="top:29px">Disclaimer</p>
  <p class="note" style="top:39px">Any dissemination of results reflects only the author's view and the Tarvell Council is not responsible for any use that may be made of the information it contains.</p>
  <p class="label" style="top:59px">Copyright message</p>
  <p class="note" style="top:69px"><b>© VARDEN Consortium, 2019</b><br>This deliverable contains original unpublished work except where clearly indicated otherwise. Acknowledgement of previously published material and of the work of others has been made through appropriate citation, quotation or both. Reproduction is authorised provided the source is acknowledged.</p>
  <p class="label" style="top:103px">Document information</p>
  <table class="grid" style="top:113px">
    <tr><th>Grant Agreement Number</th><th>804417</th><th>Acronym</th><th>VARDEN</th></tr>
    <tr><td class="key">Full Title</td><td colspan="3">An Integrated Cyber Defence Kit for Clinical Networks</td></tr>
    <tr><td class="key tall">Topic</td><td colspan="3">CX-HLT-07-2019 Framework for evaluating and lowering digital threats in clinics and care homes to safeguard records/systems/networks</td></tr>
    <tr><td class="key">Funding scheme</td><td colspan="3">RIA - Research and Innovation action</td></tr>
    <tr><td class="key">Start Date</td><td>1<sup>st</sup> January 2019</td><td>Duration</td><td>36 months</td></tr>
    <tr><td class="key">Project URL</td><td colspan="3"></td></tr>
    <tr><td class="key">KR Project Officer</td><td colspan="3"></td></tr>
    <tr><td class="key">Project Coordinator</td><td colspan="3"></td></tr>
    <tr><td class="key">Deliverable</td><td colspan="3">Dx.x. Title</td></tr>
    <tr><td class="key">Work Package</td><td colspan="3">WPx – Title</td></tr>
    <tr><td class="key">Date of Delivery</td><td>Contractual &nbsp; &nbsp; &nbsp; Mx</td><td colspan="2">Actual</td></tr>
    <tr><td class="key">Nature</td><td>R - Report</td><td><b>Dissemination Level</b></td><td>P - Public</td></tr>
    <tr><td class="key">Lead Beneficiary</td><td colspan="3"></td></tr>
    <tr><td class="key">Responsible Author</td><td></td><td>Email</td><td></td></tr>
    <tr><td class="key"></td><td></td><td>Phone</td><td></td></tr>
    <tr><td class="key">Reviewer(s):</td><td colspan="3"></td></tr>
    <tr><td class="key">Keywords</td><td colspan="3"></td></tr>
  </table>
  <div class="foot"><span class="flag" role="img" aria-label="KR flag"></span><p class="foot-text">This project has received funding from the Kestral Realm's Meridian 2030 research and innovation programme under grant agreement No 804417 - Secure Systems, Resilience &amp; Digital Protection in Health and Care</p><span class="foot-page">2 of 5</span></div>
</section>

<section class="page inner p3">
  <div class="side-bar"></div>
  <div class="run-head">Dxx: Title</div><span class="head-dot"></span>
  <p class="label plain" style="top:29px">Document History</p>
  <table class="grid history" style="top:38px">
    <tr><th>Version</th><th>Issue Date</th><th>Stage</th><th style="text-align:center">Changes</th><th style="text-align:center">Contributor</th></tr>
    <tr><td class="c">1.0</td><td></td><td><b>Draft</b></td><td></td><td></td></tr>
    <tr><td class="c">2.0</td><td></td><td><b>Final</b></td><td></td><td></td></tr>
    <tr><td></td><td></td><td></td><td></td><td></td></tr>
    <tr><td></td><td></td><td></td><td></td><td></td></tr>
    <tr><td></td><td></td><td></td><td></td><td></td></tr>
  </table>
  <div class="foot"><span class="flag" role="img" aria-label="KR flag"></span><p class="foot-text">This project has received funding from the Kestral Realm's Meridian 2030 research and innovation programme under grant agreement No 804417 - Secure Systems, Resilience &amp; Digital Protection in Health and Care</p><span class="foot-page">3 of 5</span></div>
</section>

<section class="page inner p4">
  <div class="side-bar"></div>
  <div class="run-head">Dxx: Title</div><span class="head-dot"></span>
  <h2 class="toc-title">Table of Contents</h2>
  <ul class="toc">
    <li class="lvl1">Type chapter title (level 1)<span class="dots"></span>1</li>
    <li class="lvl2">Type chapter title (level 2)<span class="dots"></span>2</li>
    <li class="lvl2">Type chapter title (level 3)<span class="dots"></span>3</li>
    <li class="lvl1">Type chapter title (level 1)<span class="dots"></span>4</li>
    <li class="lvl2">Type chapter title (level 2)<span class="dots"></span>5</li>
    <li class="lvl2">Type chapter title (level 3)<span class="dots"></span>6</li>
  </ul>
  <div class="foot"><span class="flag" role="img" aria-label="KR flag"></span><p class="foot-text">This project has received funding from the Kestral Realm's Meridian 2030 research and innovation programme under grant agreement No 804417 - Secure Systems, Resilience &amp; Digital Protection in Health and Care</p><span class="foot-page">4 of 5</span></div>
</section>

<section class="page inner p5">
  <div class="end-brand"><span class="brand-dot"></span><span class="brand-name">VARDEN</span></div>
  <div class="end-band"></div>
</section>

</body>
</html>
```